New Website Design for Rides for Heroes.org - A Site for People to Donate Cars to War / Disabled Ve

Current site: www.ridesforheroes.org; Look at these sites for ideas: bikez2tots.org; gearsforhopes.org; www.autosformarines.org; www.trucksforsoldiers.org

Industry/Entity Type

Charity

Coding

Coded - Design and coding required

Number of Pages Required

1 page

Requirements
Must have
• n/a
Nice to have
• n/a
Should not have
• n/a

```html
<!DOCTYPE html>
<html lang="en">
<head>
<meta charset="utf-8">
<title>Rides for Heroes – Donate Your Car</title>
<link href="https://fonts.googleapis.com/css2?family=Roboto:wght@300;400;500;700&family=Arvo:wght@400;700&display=swap" rel="stylesheet">
<style>
:root{
  --blue:#1a73c9;
  --blue-dark:#0d4f9e;
  --blue-light:#2f8ee0;
  --red:#b81414;
  --text:#555;
  --muted:#777;
  --line:#d8d8d8;
  --gray-bg:#f1f1f1;
  --footer:#2a2a2a;
  --white:#fff;
}
*{box-sizing:border-box;margin:0;padding:0}
html,body{width:726px;height:1200px;overflow:hidden}
body{position:relative;font-family:'Roboto',sans-serif;color:var(--text);background:var(--white)}
.abs{position:absolute}
a{color:inherit;text-decoration:none}

/* header */
.header{left:0;top:0;width:726px;height:92px;background:linear-gradient(180deg,#3c8be0,#1560bd)}
.brand{left:33px;top:20px;display:flex;align-items:center;gap:8px}
.brand-mark{width:22px;height:22px;background:var(--white)}
.brand-name{font-size:22px;font-weight:500;color:var(--white)}
.helpline{left:510px;top:20px;text-align:left;color:var(--white)}
.helpline p{font-size:12px;font-weight:300}
.helpline strong{display:block;font-size:14px;font-weight:500;letter-spacing:.3px;margin-top:5px}
.agent{left:626px;top:0;width:70px;height:92px;background:linear-gradient(180deg,#c9a78e,#6d5446);border-radius:30px 30px 0 0}

/* nav */
.nav{left:33px;top:77px;width:667px;height:30px;background:var(--white);border-radius:3px;box-shadow:0 1px 3px rgba(0,0,0,.25);display:flex;align-items:center}
.nav a{font-size:9.5px;color:#666;text-transform:uppercase;padding:0 12.5px;height:24px;line-height:24px}
.nav a.active{background:var(--red);color:var(--white);font-weight:700;margin-left:3px}
.nav .donate{margin-left:auto;margin-right:3px;background:var(--blue-dark);color:var(--white);font-weight:700;font-size:10.5px;padding:0 14px}

/* hero */
.hero{left:0;top:107px;width:726px;height:217px;background:linear-gradient(90deg,#3a3a3f,#55504c 45%,#2c2c30)}
.hero-title{left:387px;top:144px;color:var(--white);text-transform:uppercase}
.hero-title .lead{font-family:'Arvo',serif;font-size:21px;font-weight:400;letter-spacing:.3px}
.hero-title .big{font-family:'Arvo',serif;font-size:25px;font-weight:700;line-height:33px;letter-spacing:.4px}
.hero-car{left:356px;top:255px;width:334px;height:126px;background:radial-gradient(ellipse at 55% 55%,#2d2d30,#0e0e10 60%,rgba(0,0,0,0) 72%)}
.below-hero{left:0;top:324px;width:726px;height:279px;background:var(--gray-bg)}

/* form */
.form-card{left:33px;top:145px;width:321px;height:246px;background:var(--white);box-shadow:0 4px 6px rgba(0,0,0,.18)}
.form-card h2{position:absolute;left:33px;top:11px;font-size:18px;font-weight:500;color:var(--blue);text-transform:uppercase}
.field{position:absolute;width:141px;height:23px;border:1px solid #ccc;font-size:9px;color:#888;padding-left:8px;line-height:21px}
.field.select::after{content:"";position:absolute;right:8px;top:9px;border:4px solid transparent;border-top-color:#999}
.form-submit{position:absolute;left:169px;top:192px;width:108px;height:28px;background:var(--red);color:var(--white);font-size:13px;font-weight:500;text-align:center;line-height:28px}
.terms{position:absolute;left:169px;top:224px;font-size:7.5px;color:#999}
.form-sketch{position:absolute;left:2px;top:180px;width:150px;height:62px;background:linear-gradient(90deg,#f4f4f4,#fafafa);border-radius:40px 40px 8px 8px}

/* section titles */
.section-title{left:0;width:726px;text-align:center;font-size:15px;font-weight:300;color:#666;text-transform:uppercase}
.section-title span{color:var(--red);font-weight:400}
.section-title::after{content:"";display:block;width:143px;height:2px;background:#ccc;margin:7px auto 0}

/* how it works */
.step{top:465px;width:200px;text-align:center}
.step svg{display:block;margin:0 auto}
.step h3{font-size:15px;font-weight:300;margin-top:9px}
.step p{font-size:9.2px;line-height:15px;color:#666;margin-top:5px}
.step .more{display:block;font-size:8px;color:#444;margin-top:11px}
.red{color:var(--red)}.blue{color:var(--blue)}

/* why donate */
.reason{width:325px;display:flex;gap:14px;border-bottom:1px solid var(--line);padding-bottom:12px}
.reason svg{flex:none}
.reason h4{font-size:10.5px;font-weight:400;color:var(--blue)}
.reason p{font-size:8.4px;line-height:13px;color:#666;margin-top:4px}

/* trust */
.trust-bg{left:0;top:915px;width:726px;height:133px;background:var(--gray-bg)}
.panel{top:940px;width:318px;height:85px;background:var(--white);border:1px solid #ccc;border-radius:4px;overflow:hidden}
.panel h5{height:25px;line-height:26px;background:var(--blue);color:var(--white);font-size:13px;font-weight:300;padding-left:14px;text-transform:uppercase}
.badges{display:flex;align-items:center;justify-content:space-around;height:58px}
.badge-rect{width:80px;height:30px;background:#4a9ed8;border-radius:3px}
.badge-circle{width:26px;height:26px;border-radius:50%;background:#5aa9c8}
.badge-seal{width:44px;height:44px;border-radius:50%;border:3px dotted #4f7fa8}
.badge-shield{width:90px;height:30px;background:#555;border-radius:3px}
.program{display:flex;justify-content:space-around;padding-top:8px}
.program div{text-align:center;font-size:6px;color:#777;width:60px;line-height:7px}
.program svg{display:block;margin:0 auto 3px}

/* footer */
.footer{left:0;top:1048px;width:726px;height:152px;background:var(--footer);color:#aaa}
.foot-nav{position:absolute;left:0;top:16px;width:726px;text-align:center;font-size:9px;color:#aaa}
.foot-nav a{margin:0 6px}
.foot-nav a:first-child{color:var(--white)}
.foot-nav i{font-style:normal;color:#888}
.foot-rule{position:absolute;left:33px;top:40px;width:667px;height:1px;background:#555}
.foot-h{position:absolute;top:60px;font-size:11.5px;color:var(--blue-light);font-weight:400}
.newsletter{position:absolute;left:33px;top:78px;width:208px;height:23px;border:1px solid #555;font-size:9px;color:#888;line-height:21px;padding-left:6px}
.newsletter b{position:absolute;right:-1px;top:-1px;width:28px;height:23px;background:var(--blue-light)}
.social{position:absolute;left:33px;top:116px;display:flex;gap:6px}
.social span{width:19px;height:19px;border-radius:50%;border:1px solid #777}
.social span:first-child{background:var(--blue-light);border-color:var(--blue-light)}
.contact{position:absolute;left:328px;top:80px;width:179px;font-size:8.6px;color:#ccc}
.contact div{display:flex;align-items:center;gap:7px;height:22px;border-bottom:1px solid #444}
.contact div:last-child{border:none}
.foot-brand{position:absolute;left:586px;top:58px;display:flex;align-items:center;gap:5px;font-size:10px;color:var(--white);font-weight:500}
.foot-brand i{width:10px;height:10px;background:var(--white)}
.copy{position:absolute;left:589px;top:112px;font-size:7.5px;line-height:13px;color:#aaa}
</style>
</head>
<body>

<header class="abs header">
  <div class="abs brand"><span class="brand-mark"></span><span class="brand-name">Rides for Heroes</span></div>
  <div class="abs helpline"><p>We need your help</p><strong>1-800-555-0142</strong></div>
  <div class="abs agent" role="img" aria-label="Photo of a support agent wearing a headset"></div>
</header>

<nav class="abs nav">
  <a class="active" href="#">Home</a>
  <a href="#">Why Donate Your Car</a>
  <a href="#">About Our Charity</a>
  <a href="#">F.A.Q.</a>
  <a href="#">Blog</a>
  <a href="#">Contact Us</a>
  <a class="donate" href="#">Donate Now</a>
</nav>

<div class="abs hero" role="img" aria-label="Blurred city street photo"></div>
<div class="abs below-hero"></div>
<div class="abs hero-title">
  <div class="lead">Donate your car:</div>
  <div class="big">Full tax deduction</div>
  <div class="big">Running or not</div>
</div>
<div class="abs hero-car" role="img" aria-label="Photo of a black sedan"></div>

<form class="abs form-card">
  <div class="form-sketch" role="img" aria-label="Faint sketch of a sports car"></div>
  <h2>Donating is simple</h2>
  <div class="field" style="left:11px;top:47px">Name</div>
  <div class="field" style="left:169px;top:47px">Email:</div>
  <div class="field" style="left:11px;top:81px">Phone Number</div>
  <div class="field" style="left:169px;top:81px">Cell Phone</div>
  <div class="field" style="left:11px;top:116px">Address</div>
  <div class="field" style="left:169px;top:116px">City</div>
  <div class="field select" style="left:11px;top:150px">State</div>
  <div class="field" style="left:169px;top:150px">Zip Code</div>
  <div class="form-submit">DONATE NOW</div>
  <div class="terms">*Terms &amp; Conditions apply</div>
</form>

<h2 class="abs section-title" style="top:417px">Car donation <span>how it works</span></h2>

<div class="abs step" style="left:20px">
  <svg width="44" height="36" viewBox="0 0 44 36"><circle cx="24" cy="14" r="12" fill="#b81414"/><text x="24" y="19" font-size="14" text-anchor="middle" fill="#fff" font-family="Roboto,sans-serif">€</text><path d="M4 28c8-6 14-2 20 0h14c-2 4-10 7-22 6z" fill="#b81414"/></svg>
  <h3 class="red">Donate</h3>
  <p>Lorem ipsum dolor sit amet, consectetur<br>adipiscing elit mauris pellentesque,</p>
  <a class="more" href="#">Read more</a>
</div>
<div class="abs step" style="left:266px">
  <svg width="36" height="36" viewBox="0 0 36 36"><path d="M6 4l18-2 6 30-18 2z" fill="none" stroke="#1a73c9" stroke-width="2.5"/><path d="M11 10h11M12 15h11M13 20h11" stroke="#1a73c9" stroke-width="2"/></svg>
  <h3 class="blue">Deductible Receipt</h3>
  <p>Lorem ipsum dolor sit amet, consectetur<br>adipiscing elit mauris pellentesque,</p>
  <a class="more" href="#">Read more</a>
</div>
<div class="abs step" style="left:500px">
  <svg width="40" height="36" viewBox="0 0 40 36"><circle cx="20" cy="9" r="6" fill="#1a73c9"/><path d="M2 10l4 0 6 12 5 4v8h-6v-6L3 20zM38 10l-4 0-6 12-5 4v8h6v-6l8-8z" fill="#1a73c9"/></svg>
  <h3 class="blue">Help</h3>
  <p>Lorem ipsum dolor sit amet, consectetur<br>adipiscing elit mauris pellentesque,</p>
  <a class="more" href="#">Read more</a>
</div>

<h2 class="abs section-title" style="top:624px">Why donate <span>your car to us?</span></h2>

<div class="abs reason" style="left:33px;top:663px">
  <svg width="40" height="34" viewBox="0 0 40 34"><rect x="2" y="4" width="18" height="26" rx="2" fill="#1a73c9"/><circle cx="30" cy="14" r="8" fill="#444"/><path d="M26 14h8M30 10v8" stroke="#fff" stroke-width="2"/></svg>
  <div><h4>Trusted Bureau A+ Rated &amp; IRS 501(c)3 Approved:</h4><p>Free 24/7 Pickup with No DMV Hassles.</p></div>
</div>
<div class="abs reason" style="left:33px;top:718px">
  <svg width="40" height="34" viewBox="0 0 40 34"><circle cx="18" cy="16" r="13" fill="none" stroke="#333" stroke-width="3"/><circle cx="18" cy="16" r="5" fill="#1a73c9"/></svg>
  <div><h4>Free Local Towing:</h4><p>We will pick up your car donation, running or not, when it's most convenient, at home or work.</p></div>
</div>
<div class="abs reason" style="left:33px;top:789px">
  <svg width="40" height="30" viewBox="0 0 40 30"><path d="M2 22l4-8h20l6 8z" fill="#444"/><circle cx="10" cy="24" r="3" fill="#444"/><circle cx="26" cy="24" r="3" fill="#444"/><path d="M16 14l5 8 12-18" fill="none" stroke="#1a73c9" stroke-width="3.5"/></svg>
  <div><h4>All Cars Accepted:</h4><p>We take your car regardless of its condition or registration status.</p></div>
</div>
<div class="abs reason" style="left:33px;top:847px;border:none">
  <svg width="40" height="40" viewBox="0 0 40 40"><text x="1" y="10" font-size="9" font-weight="700" fill="#1a73c9" font-family="Roboto,sans-serif">TAX%</text><circle cx="15" cy="16" r="3" fill="#333"/><path d="M7 20h16M15 20v10l-4 8M15 30l4 8" stroke="#333" stroke-width="3" fill="none"/></svg>
  <div><h4>Income Tax Deduction:</h4><p>We issue you an IRS tax receipt &amp; offer the largest resale network to get you the highest tax write-off possible.</p></div>
</div>

<div class="abs reason" style="left:377px;top:663px;width:323px">
  <svg width="40" height="34" viewBox="0 0 40 34"><rect x="10" y="4" width="22" height="26" rx="2" fill="none" stroke="#333" stroke-width="2.5"/><path d="M2 26l16-16" stroke="#1a73c9" stroke-width="4"/></svg>
  <div><h4>No Paperwork Hassles:</h4><p>We take any car and handle everything: DMV, Smog and IRS paperwork.</p></div>
</div>
<div class="abs reason" style="left:377px;top:735px;width:323px">
  <svg width="40" height="40" viewBox="0 0 40 40"><circle cx="8" cy="8" r="4" fill="#1a73c9"/><path d="M12 8h14" stroke="#1a73c9" stroke-width="3"/><path d="M4 30l4-10h18l4 10v6H4z" fill="#333"/></svg>
  <div><h4>Car donations help fund programs:</h4><p>And benefit National Heroes Support Fund. An IRS 501(c)3 nonprofit organization.</p></div>
</div>
<div class="abs reason" style="left:377px;top:806px;width:323px">
  <svg width="40" height="40" viewBox="0 0 40 40"><rect x="3" y="6" width="26" height="24" rx="2" fill="none" stroke="#1a73c9" stroke-width="3"/><path d="M3 13h26" stroke="#1a73c9" stroke-width="3"/><circle cx="28" cy="29" r="8" fill="#fff" stroke="#333" stroke-width="2.5"/><path d="M28 24v5h4" stroke="#333" stroke-width="2" fill="none"/></svg>
  <div><h4>Schedule a Free Pickup:</h4><p>Complete the form and a representative will call you to arrange a convenient time to pickup your car.</p></div>
</div>

<div class="abs trust-bg"></div>
<section class="abs panel" style="left:33px">
  <h5>Safe &amp; Secure</h5>
  <div class="badges">
    <span style="display:flex;gap:4px;align-items:center"><span class="badge-rect"></span><span class="badge-circle"></span></span>
    <span class="badge-seal"></span>
    <span class="badge-shield"></span>
  </div>
</section>
<section class="abs panel" style="left:382px">
  <h5>Car Donation Program</h5>
  <div class="program">
    <div><svg width="32" height="20" viewBox="0 0 32 20"><path d="M2 4l14-2 14 4-4 12-10-2-12-2z" fill="#4f7fb5"/></svg>Donations accepted nationwide</div>
    <div><svg width="32" height="20" viewBox="0 0 32 20"><path d="M2 16V8l6-6h18l4 6v8z" fill="none" stroke="#4f7fb5" stroke-width="2"/><circle cx="9" cy="16" r="3" fill="#4f7fb5"/><circle cx="24" cy="16" r="3" fill="#4f7fb5"/></svg>All vehicle types welcome</div>
    <div><svg width="32" height="22" viewBox="0 0 32 22"><rect x="9" y="1" width="14" height="19" rx="1" fill="none" stroke="#4f7fb5" stroke-width="2"/><path d="M12 7h8M12 11h8M12 15h6" stroke="#4f7fb5" stroke-width="1.5"/></svg>Tax deductible</div>
    <div><svg width="32" height="20" viewBox="0 0 32 20"><path d="M2 14h20V6h5l3 5v3" fill="none" stroke="#4f7fb5" stroke-width="2"/><path d="M4 2l8 10" stroke="#4f7fb5" stroke-width="2"/><circle cx="8" cy="16" r="2.5" fill="#4f7fb5"/><circle cx="25" cy="16" r="2.5" fill="#4f7fb5"/></svg>Towing is free</div>
  </div>
</section>

<footer class="abs footer">
  <nav class="foot-nav"><a href="#">Home</a><i>/</i><a href="#">Why Donate Your Car</a><i>/</i><a href="#">About Our Charity</a><i>/</i><a href="#">F.A.Q.</a><i>/</i><a href="#">Blog</a><i>/</i><a href="#">Contact Us</a><i>/</i><a href="#">Privacy Policy</a></nav>
  <div class="foot-rule"></div>
  <h6 class="foot-h" style="left:33px">Subscribe to our Newsletter</h6>
  <div class="newsletter">@email_address<b><svg width="28" height="23" viewBox="0 0 28 23"><path d="M7 12l14-6-4 12-3-4z" fill="#fff"/></svg></b></div>
  <div class="social"><span></span><span></span><span></span><span></span></div>
  <h6 class="foot-h" style="left:328px">Contact</h6>
  <div class="contact">
    <div><svg width="10" height="10" viewBox="0 0 10 10"><path d="M5 0a3.5 3.5 0 0 1 3.5 3.5C8.5 6 5 10 5 10S1.5 6 1.5 3.5A3.5 3.5 0 0 1 5 0z" fill="#2f8ee0"/></svg>11th lorem ispum USA Sydeny, Canada</div>
    <div><svg width="10" height="10" viewBox="0 0 10 10"><path d="M2 0l2 3-1 1.5c.8 1.4 1.6 2.2 2.5 2.5L7 6l3 2-1.5 2C4 10 0 6 0 1.5z" fill="#2f8ee0"/></svg>1 800 555 0142</div>
    <div><svg width="10" height="8" viewBox="0 0 10 8"><rect width="10" height="8" fill="#2f8ee0"/><path d="M0 0l5 4 5-4" stroke="#fff" fill="none"/></svg>info@ridesforheroes.org</div>
  </div>
  <div class="foot-brand"><i></i>Rides for Heroes</div>
  <p class="copy">© 2016 Rides For Heroes.<br>All Rights Reserved.</p>
</footer>

</body>
</html>
```